I need a flyer that is professional, advertises and informs people about my health coaching practice. I am a Nationally Board Certified Health and Wellness Coach, lifestyle medicine certified and a lifestyle coach for the NHQ's Glucose Steady Initiative. I have my Master's Degree in Counseling Psychology. The final design should communicate evidence based health coaching that is self-directed and aimed at creating lasting health behavioral changes designed to enhance well-being. I am very open in terms of design but really would like a professional look to the flyer. I did want my contact information on the flyer: dana@vitalpathrecords.com and (217) 555-0148

Target Market(s)

Adults looking to improve their health, decrease risk factors for lifestyle disease, reduce weight, make better lifestyle choices to improve well-being.

Industry/Entity Type

Health And Wellness

Font styles to use
Sans Serif

Colors

Designer to choose colors to be used in the design.

Requirements
Must have
• Services offered, a professional feel, Dana Morrow Health Coaching (name of my practice), my phone number (217) 555-0148 and email: dana@vitalpathrecords.com, location: 1873 W Larkfield Avenue Bloomington IL 61709 my website: danamorrow.com to schedule appointments
Nice to have
• What is Health Coaching? Health and Wellness Coaches partner with clients seeking self-directed, lasting changes, aligned with their values, which promote health and wellness and, thereby, enhance well-being. In the course of their work health and wellness coaches display unconditional positive regard for their clients and a belief in their capacity for change, and honoring that each client is an expert on his or her life, while ensuring that all interactions are respectful and non-judgmental.

```html
<!DOCTYPE html>
<html lang="en">
<head>
<meta charset="utf-8">
<title>Dana Morrow Health Coaching – Flyer</title>
<link rel="stylesheet" href="https://fonts.googleapis.com/css2?family=Tinos:wght@400;700&family=Open+Sans:wght@400;600;700&display=swap">
<style>
  :root {
    --brand-blue: #1a82d8;
    --ink: #2b2b2b;
    --panel-grey: #dde1e3;
    --footer-dark: #3f3f40;
    --paper: #ffffff;
    --serif: "Tinos", "Times New Roman", serif;
    --sans: "Open Sans", Arial, sans-serif;
  }
  * { margin: 0; padding: 0; box-sizing: border-box; }
  html, body { width: 800px; height: 1200px; overflow: hidden; background: var(--paper); }
  .flyer { position: relative; width: 800px; height: 1200px; background: var(--paper); color: var(--ink); font-family: var(--sans); }

  .practice-name { position: absolute; top: 20px; left: 0; width: 800px; text-align: center; font-family: var(--serif); font-weight: 400; font-size: 32px; color: var(--brand-blue); }

  .hero-photo { position: absolute; top: 84px; left: 0; width: 800px; height: 384px;
    background: radial-gradient(ellipse at 68% 40%, #fbfbf2 0%, #eef1e4 18%, #a9d4e6 42%, #3f8fc6 70%, #2b6fae 100%); }
  .hero-banner { position: absolute; top: 231px; left: 0; width: 520px; height: 236px; background: rgba(26,130,216,0.88); color: #fff; padding: 28px 0 0 34px; }
  .hero-title { font-family: var(--serif); font-weight: 400; font-size: 50px; line-height: 66px; letter-spacing: -0.5px; }
  .hero-tagline { margin-top: 14px; font-size: 19px; }

  .section-heading { font-family: var(--serif); font-weight: 400; color: var(--brand-blue); text-transform: uppercase; font-size: 26px; }
  .intro { position: absolute; top: 496px; left: 34px; width: 732px; }
  .intro p { margin-top: 14px; font-size: 11.6px; line-height: 15px; }

  .services { position: absolute; top: 646px; left: 34px; width: 340px; }
  .service { margin-top: 10px; }
  .service:first-of-type { margin-top: 14px; }
  .service-head { display: flex; justify-content: space-between; align-items: center; }
  .service-head.tag-row { justify-content: flex-end; margin-top: 4px; }
  .service-name { font-family: var(--serif); color: var(--brand-blue); font-size: 13.5px; }
  .price-tag { background: var(--brand-blue); color: #fff; font-size: 8.5px; width: 60px; height: 18px; line-height: 18px; text-align: center; }
  .service-desc { font-size: 11px; line-height: 14px; margin-top: 5px; }

  .highlights { position: absolute; top: 685px; left: 411px; width: 389px; height: 384px; }
  .highlight { position: relative; background: var(--panel-grey); height: 186px; padding: 22px 20px 0 20px; }
  .highlight + .highlight { margin-top: 12px; }
  .highlight .section-heading { font-size: 24px; }
  .highlight-body { display: flex; align-items: flex-start; margin-top: 18px; }
  .highlight-photo { flex: none; width: 96px; height: 96px; border-radius: 50%; border: 3px solid var(--brand-blue); }
  .photo-outdoor { background: radial-gradient(circle at 50% 35%, #f4f1d8 0%, #8fae6e 35%, #4f6b3e 70%, #a99a7a 100%); }
  .photo-water { background: radial-gradient(circle at 45% 45%, #ffffff 0%, #cfe6f4 40%, #7fb6dc 75%, #4f90c4 100%); }
  .highlight-text { margin-left: 30px; font-size: 11px; line-height: 14px; text-align: justify; }

  .cta { position: absolute; top: 1117px; left: 85px; width: 632px; height: 28px; background: var(--brand-blue); color: #fff; display: flex; align-items: center; justify-content: center; gap: 22px; z-index: 2; }
  .cta-label { font-size: 12px; font-weight: 600; text-transform: uppercase; }
  .cta-url { font-size: 19px; }
  .contact-bar { position: absolute; top: 1130px; left: 0; width: 800px; height: 70px; background: var(--footer-dark); color: #fff; display: flex; align-items: flex-end; justify-content: space-between; padding: 0 34px 22px; font-size: 12px; }
  .contact-item { display: flex; align-items: center; gap: 10px; }
  .contact-item svg { width: 16px; height: 16px; fill: #fff; }
</style>
</head>
<body>
<main class="flyer">
  <header>
    <h1 class="practice-name">Dana Morrow Health Coaching</h1>
  </header>

  <div class="hero-photo" role="img" aria-label="Close-up photo of a white water lily on blue water"></div>
  <section class="hero-banner">
    <h2 class="hero-title">Health Coaching is<br>Embracing Your Health</h2>
    <p class="hero-tagline">Let us help you build the healthy life you desereve !</p>
  </section>

  <section class="intro">
    <h2 class="section-heading">What is Health Coaching?</h2>
    <p>Health and Wellness Coaches partner with clients seeking self-directed, lasting changes, aligned with their values, which promote health and wellness and, thereby, enhance well-being. In the course of their work health and wellness coaches display unconditional positive regard for their clients and a belief in their capacity for change, and honoring that each client is an expert on his or her life, while ensuring that all interactions are respectful and non-judgemental.</p>
  </section>

  <section class="services">
    <h2 class="section-heading">Our Services</h2>
    <div class="service">
      <div class="service-head"><span class="service-name">Health Coaching Data Collection</span><span class="price-tag">1hr/$199</span></div>
      <p class="service-desc">Evidence based health coaching is based in data. With the appropriate data, we can work together to reduce your risk for lifestyle disease.</p>
    </div>
    <div class="service">
      <div class="service-head"><span class="service-name">Health Coaching Initial Consultation</span><span class="price-tag">30 min free</span></div>
      <p class="service-desc">Want to know if health coaching is right for you? I invite you to schedule an initial consultation with me.</p>
    </div>
    <div class="service">
      <div class="service-head"><span class="service-name">Individual Health Coaching 30 Minute Session</span><span class="price-tag">30 min/$50</span></div>
      <p class="service-desc">Partner with a Nationally Registered Lifestyle and Wellness Coach (NRLWC) for clients seeking self-directed</p>
    </div>
    <div class="service">
      <div class="service-head"><span class="service-name">Health Coaching Package - Six 30 Minute Sessions</span></div>
      <div class="service-head tag-row"><span class="price-tag">30 min/$275</span></div>
      <p class="service-desc">A focused health coaching session on the topics of your choice. Designed to get results, this package is shaped and molded around your goals and progress.</p>
    </div>
    <div class="service">
      <div class="service-head"><span class="service-name">NHQ Glucose Steady Lifestyle 16 Week Program</span></div>
      <div class="service-head tag-row"><span class="price-tag">1hr/$249</span></div>
      <p class="service-desc">Developed by the National Health Quorum (NHQ), a proven program to prevent or delay Type 2 Diabetes.</p>
    </div>
  </section>

  <aside class="highlights">
    <div class="highlight">
      <h3 class="section-heading">Wellness Experience</h3>
      <div class="highlight-body">
        <div class="highlight-photo photo-outdoor" role="img" aria-label="Round photo of a sunlit outdoor path among trees"></div>
        <p class="highlight-text">Extensive experience allows me to guide you. My client success stories reflect my ability to, time after time, help clients improve their health and achieve a higher level of life satisfaction.</p>
      </div>
    </div>
    <div class="highlight">
      <h3 class="section-heading">Active Coaching</h3>
      <div class="highlight-body">
        <div class="highlight-photo photo-water" role="img" aria-label="Round photo of hands with clear water"></div>
        <p class="highlight-text">My education and training completes my coaching arsenal - allowing me to provide you, the client, with the tools and methods you need to achieve your goals.</p>
      </div>
    </div>
  </aside>

  <div class="cta">
    <span class="cta-label">To schedule appointments visit our website</span>
    <span class="cta-url">www.danamorrow.com</span>
  </div>

  <footer class="contact-bar">
    <span class="contact-item">
      <svg viewBox="0 0 24 24" aria-hidden="true"><path d="M6.6 10.8a15.1 15.1 0 0 0 6.6 6.6l2.2-2.2c.3-.3.7-.4 1-.2 1.1.4 2.3.6 3.6.6.6 0 1 .4 1 1V20c0 .6-.4 1-1 1A17 17 0 0 1 3 4c0-.6.4-1 1-1h3.5c.6 0 1 .4 1 1 0 1.3.2 2.5.6 3.6.1.3 0 .7-.2 1z"/></svg>
      (217) 555-0148
    </span>
    <span class="contact-item">
      <svg viewBox="0 0 24 24" aria-hidden="true"><path d="M2 5h20v14H2z M4 7v1l8 5 8-5V7l-8 5z" fill-rule="evenodd"/></svg>
      dana@vitalpathrecords.com
    </span>
    <span class="contact-item">
      <svg viewBox="0 0 24 24" aria-hidden="true"><path d="M12 2a7 7 0 0 0-7 7c0 5 7 13 7 13s7-8 7-13a7 7 0 0 0-7-7zm0 9.5A2.5 2.5 0 1 1 12 6.5a2.5 2.5 0 0 1 0 5z"/></svg>
      1873 W Larkfield Avenue Bloomington IL 61709
    </span>
  </footer>
</main>
</body>
</html>
```